Namecard with Logo for NanoTechnology Business

We wish to invite you to propose a creative Logo design compatible with the namecard design that suits our business. (you may take inspiration from fullerene's molecular structure, but since one of our partner company already has a fullerene-logo, please don't propose anything similar to those. see attached image logo of "QRV")
You do not have to be constrained by a 'ball shaped' design requirement. You can play with the idea of a molecule, but high tech and creative.

Target Market(s)

lubricant market

Contact Information for Business Card

For the Front, instead of accentuating the company name, we would like instead to display the following words more prominently and creatively stylized and centered.

"Full Guard Surface Restoration" (these words bigger)
"bring your engine back to life" (these words smaller and right below the words above, and with small letters)

The following contact details can be smaller compared to the emphasis above

Name detail: Lionel Brask
Company detail: Velun Fidor Singapore Pte Ltd
Headquarter detail: 17 Corwell Industrial Park B, S530942
Mobile detail: (65) 83527960
Website: (to be confirmed)

For the Back of the namecard, there are to be two headings. Many words involved. Okay for the words to be smaller. Two columns please.

Column Heading#1; Market Sectors
Indented Words;
Bearings
Fleet Management
Trucks and Buses
Conveyor Systems
Gears and Gear Boxes
Heavy Machinery
Mining
Oil and Gas Drilling
Metal Forming
Steel Mills
Power Generation Plants
Railroad
Moving Freight
Space and Defence Industry
Wind Turbines

Column Heading#2; Oil Quality Research Laboratory for Condition Monitoring of Wear and Tear Sampling Analysis
Indented words;
Spectrographic Analysis
Infra-Red Spectroscopy
Otto Brenwald Titration (H2O Content)
Viscosity Analysis
Ferrous Debris Monitoring
ISO 4406 Cleanliness Code
Wear Debris Analysis

We wish to include the logo of our partner companies (bottom of back)

Logo 1 - QRV Logo, with the accompanying words (Sole-Source Patented Technology)

Logo 2 - Brivalorex Logo, with the accompany words (Preferred Knowledge Partner)

Colors

Designer to choose colors to be used in the design.

Requirements
Must have
• words as provided
Nice to have
• the key to this project is a creative logo that suits our business
Should not have
• logo similar to attached

```html
<!DOCTYPE html>
<html lang="en">
<head>
<meta charset="utf-8">
<title>Full Guard Surface Restoration – Namecard</title>
<link rel="stylesheet" href="https://fonts.googleapis.com/css2?family=Exo+2:wght@300;800&family=Open+Sans:wght@400;700&family=Josefin+Sans:wght@400;600&display=swap">
<style>
  :root {
    --page-bg: #e9e6e1;
    --card-bg: #0a0a0a;
    --brand-blue: #1f78c8;
    --text-white: #f4f4f4;
    --text-grey: #b9b9b9;
  }
  * { margin: 0; padding: 0; box-sizing: border-box; }
  html, body { width: 1200px; height: 900px; overflow: hidden; background: var(--page-bg); }
  .canvas { position: relative; width: 1200px; height: 900px; }
  .card {
    position: absolute; left: 230px; width: 740px; height: 420px;
    background: var(--card-bg); box-shadow: 0 6px 18px rgba(0,0,0,.25);
    overflow: hidden;
  }
  .card--front { top: 20px; font-family: "Open Sans", sans-serif; }
  .card--back { top: 460px; font-family: "Josefin Sans", sans-serif; }

  /* Front */
  .headline {
    position: absolute; left: 70px; top: 112px; white-space: nowrap;
    font-family: "Exo 2", sans-serif; font-weight: 800; font-size: 34px;
    letter-spacing: 2.5px; color: var(--brand-blue);
  }
  .tagline {
    position: absolute; left: 72px; top: 156px; white-space: nowrap;
    font-family: "Exo 2", sans-serif; font-weight: 300; font-size: 23px;
    letter-spacing: 3px; color: var(--brand-blue);
  }
  .holder { position: absolute; left: 50px; top: 286px; width: 320px; text-align: center; }
  .holder__name { font-weight: 700; font-size: 17px; letter-spacing: 2px; color: var(--text-white); }
  .holder__company { font-size: 15px; letter-spacing: 1.5px; color: var(--text-grey); margin-top: 4px; white-space: nowrap; }
  .divider { position: absolute; left: 400px; top: 238px; width: 5px; height: 50px; background: var(--brand-blue); }
  .contact { position: absolute; left: 428px; top: 240px; }
  .contact__address { font-size: 12px; letter-spacing: 1.5px; color: var(--text-grey); white-space: nowrap; }
  .contact__phone { font-weight: 700; font-size: 17px; letter-spacing: 2px; color: var(--text-white); margin-top: 6px; text-align: right; }

  /* Back */
  .column { position: absolute; top: 34px; }
  .column--sectors { left: 58px; width: 270px; }
  .column--lab { left: 360px; width: 350px; }
  .column__heading { color: var(--text-white); font-weight: 600; letter-spacing: 3px; }
  .column--sectors .column__heading { font-size: 20px; margin-bottom: 10px; }
  .column--lab .column__heading { font-size: 22px; line-height: 27px; margin-bottom: 14px; }
  .column__list { list-style: none; color: var(--brand-blue); letter-spacing: 2px; }
  .column--sectors .column__list { font-size: 15px; line-height: 18px; padding-left: 8px; }
  .column--lab .column__list { font-size: 16px; line-height: 20px; }

  .partner { position: absolute; text-align: center; }
  .partner--qrv { left: 340px; top: 322px; width: 195px; }
  .partner--brivalorex { left: 540px; top: 336px; width: 195px; }
  .partner__mark {
    display: flex; align-items: center; justify-content: center; gap: 6px;
    color: var(--text-white); font-weight: 600; white-space: nowrap;
  }
  .partner--qrv .partner__mark { height: 54px; font-size: 34px; letter-spacing: 2px; }
  .partner--brivalorex .partner__mark { height: 38px; font-size: 11px; letter-spacing: .5px; }
  .partner__square { width: 9px; height: 9px; background: var(--brand-blue); flex: none; }
  .partner__caption { color: var(--brand-blue); font-size: 10px; letter-spacing: .5px; margin-top: 10px; white-space: nowrap; }
  .partner--brivalorex .partner__caption { margin-top: 12px; }
</style>
</head>
<body>
<main class="canvas">
  <section class="card card--front" aria-label="Namecard front">
    <h1 class="headline">Full Guard Surface Restoration</h1>
    <p class="tagline">bring your engine back to life</p>
    <div class="holder">
      <p class="holder__name">Lionel Brask</p>
      <p class="holder__company">Velun Fidor Singapore Pte Ltd</p>
    </div>
    <div class="divider"></div>
    <div class="contact">
      <p class="contact__address">17 Corwell Industrial Park B, S530942</p>
      <p class="contact__phone">(65) 83527960</p>
    </div>
  </section>

  <section class="card card--back" aria-label="Namecard back">
    <div class="column column--sectors">
      <h2 class="column__heading">Market Sectors</h2>
      <ul class="column__list">
        <li>Bearings</li>
        <li>Fleet Management</li>
        <li>Trucks and Buses</li>
        <li>Conveyor Systems</li>
        <li>Gears and Gear Boxes</li>
        <li>Heavy Machinery</li>
        <li>Mining</li>
        <li>Oil and Gas Drilling</li>
        <li>Metal Forming</li>
        <li>Steel Mills</li>
        <li>Power Generation Plants</li>
        <li>Railroad</li>
        <li>Moving Freight</li>
        <li>Space and Defence Industry</li>
        <li>Wind Turbines</li>
      </ul>
    </div>
    <div class="column column--lab">
      <h2 class="column__heading">Oil Quality Research Laboratory for Condition Monitoring of Wear and Tear Sampling Analysis</h2>
      <ul class="column__list">
        <li>Spectrographic Analysis</li>
        <li>Infra-Red Spectroscopy</li>
        <li>Otto Brenwald Titration (H2O Content)</li>
        <li>Viscosity Analysis</li>
        <li>Ferrous Debris Monitoring</li>
        <li>ISO 4406 Cleanliness Code</li>
        <li>Wear Debris Analysis</li>
      </ul>
    </div>
    <div class="partner partner--qrv">
      <div class="partner__mark">QRV</div>
      <p class="partner__caption">Sole-Source Patented Technology</p>
    </div>
    <div class="partner partner--brivalorex">
      <div class="partner__mark"><span class="partner__square"></span>BRIVALOREX INTERNATIONAL</div>
      <p class="partner__caption">Preferred Knowledge Partner</p>
    </div>
  </section>
</main>
</body>
</html>
```